Looking for a professional, clean and crisp business card

I am in the underground utilities industry and am just looking for a really impressive business card. I would like our card to be white with our symbol crisp and clear with it protruding. I also have a business partner that will require his name and info on the card once the design is set. I would like to have our website info on the card which is;
http://granitetrenchco.example/

Contact Information for Business Card

Website, contact name, number and email

```html
<!DOCTYPE html>
<html lang="en">
<head>
<meta charset="utf-8">
<title>Granite Trench Co — Business Card</title>
<link href="https://fonts.googleapis.com/css2?family=Oswald:wght@300;400;500&display=swap" rel="stylesheet">
<style>
  :root {
    --backdrop: #4470b8;
    --card-light: #ececee;
    --card-dark: #000000;
    --ink: #111111;
    --accent-blue: #3b5fa8;
    --white: #ffffff;
  }
  * { margin: 0; padding: 0; box-sizing: border-box; }
  html, body { width: 1200px; height: 1101px; overflow: hidden; }
  body {
    background: var(--backdrop);
    font-family: "Oswald", sans-serif;
    position: relative;
  }
  .card {
    position: absolute;
    width: 303px;
    height: 530px;
  }
  .card-front { left: 246px; top: 269px; background: var(--card-light); color: var(--ink); }
  .card-back  { left: 642px; top: 267px; background: var(--card-dark); color: var(--white); }

  .brand {
    position: absolute;
    left: 0; right: 0;
    display: flex;
    flex-direction: column;
    align-items: center;
    text-align: center;
    font-weight: 500;
    text-transform: uppercase;
    line-height: 1.05;
  }
  .brand-mark {
    border-radius: 50%;
    margin-bottom: 10px;
  }
  .card-front .brand { top: 82px; font-size: 34px; color: var(--ink); }
  .card-front .brand-mark { width: 34px; height: 34px; background: var(--accent-blue); }
  .card-back .brand { top: 190px; font-size: 44px; color: var(--white); }
  .card-back .brand-mark { width: 44px; height: 44px; background: var(--accent-blue); }

  .name-bar {
    position: absolute;
    left: 38px; top: 275px;
    width: 228px; height: 44px;
  }
  .name-bar .cap {
    position: absolute; top: 0;
    width: 5px; height: 44px;
    background: var(--ink);
  }
  .name-bar .cap.left { left: 0; }
  .name-bar .cap.right { right: 0; }
  .name-bar .pipe {
    position: absolute; left: 5px; right: 5px; top: 4px; bottom: 4px;
    background: var(--ink);
    border-top: 2px solid var(--card-light);
    border-bottom: 2px solid var(--card-light);
    outline: 2px solid var(--ink);
    display: flex; align-items: center; justify-content: center;
  }
  .person-name {
    color: var(--white);
    font-size: 25px;
    font-weight: 400;
    letter-spacing: 1px;
  }
  .person-role {
    position: absolute; left: 0; right: 0; top: 324px;
    text-align: center;
    font-size: 19px; font-weight: 300; letter-spacing: 0.5px;
  }
  .contact-icons {
    position: absolute; left: 38px; right: 37px; top: 371px;
    display: flex; align-items: center; gap: 9px;
  }
  .contact-icons .rule { flex: 1; height: 1px; background: var(--ink); }
  .contact-icons svg { width: 24px; height: 24px; display: block; }
  .contact-lines {
    position: absolute; left: 0; right: 0; top: 414px;
    text-align: center;
    font-size: 16px; font-weight: 300;
    line-height: 23px;
    text-transform: uppercase;
    letter-spacing: 0.2px;
  }
</style>
</head>
<body>
  <section class="card card-front">
    <div class="brand">
      <span class="brand-mark"></span>
      <span class="brand-name">Granite<br>Trench Co</span>
    </div>

    <div class="name-bar">
      <span class="cap left"></span>
      <div class="pipe"><span class="person-name">MARCUS ELLERY</span></div>
      <span class="cap right"></span>
    </div>
    <p class="person-role">PARTNER</p>

    <div class="contact-icons">
      <span class="rule"></span>
      <svg viewBox="0 0 24 24" aria-label="Phone">
        <circle cx="12" cy="12" r="12" fill="var(--accent-blue)"/>
        <path d="M8.2 6.5c.5-.4 1.1-.3 1.4.2l1 1.7c.3.5.2 1-.2 1.3l-.7.5c.6 1.4 1.7 2.6 3.1 3.3l.5-.7c.3-.4.9-.5 1.3-.2l1.7 1c.5.3.6.9.2 1.4l-.8.9c-.5.5-1.2.7-1.9.4-3-1.2-5.3-3.5-6.4-6.5-.3-.7-.1-1.4.4-1.9z" fill="var(--white)"/>
      </svg>
      <svg viewBox="0 0 24 24" aria-label="Email">
        <circle cx="12" cy="12" r="12" fill="var(--accent-blue)"/>
        <rect x="6.5" y="8" width="11" height="8" rx="1" fill="var(--white)"/>
        <path d="M6.8 8.4 12 12.6l5.2-4.2" fill="none" stroke="var(--accent-blue)" stroke-width="1.1"/>
      </svg>
      <svg viewBox="0 0 24 24" aria-label="Website">
        <circle cx="12" cy="12" r="12" fill="var(--accent-blue)"/>
        <g fill="none" stroke="var(--white)" stroke-width="1">
          <circle cx="12" cy="12" r="6"/>
          <ellipse cx="12" cy="12" rx="2.6" ry="6"/>
          <line x1="6" y1="12" x2="18" y2="12"/>
          <line x1="7" y1="9" x2="17" y2="9"/>
          <line x1="7" y1="15" x2="17" y2="15"/>
        </g>
      </svg>
      <span class="rule"></span>
    </div>

    <div class="contact-lines">
      <p>555-208-4716</p>
      <p>email@granitetrenchco.example</p>
      <p>granitetrenchco.example</p>
    </div>
  </section>

  <section class="card card-back">
    <div class="brand">
      <span class="brand-mark"></span>
      <span class="brand-name">Granite<br>Trench Co</span>
    </div>
  </section>
</body>
</html>
```